Design an attractive wine label for Brell Fine Wines

we need a wine label design, we are an Australian wine exporting company'Brell Fine Wines'. We succeed several pallets in last few months and is going to launch our first container. So it’s time to start our own brands. we will have some wines display in China's shopping mall shelves, so we want to have a catchy label which can attract Chinese eyes immediately. other details you will see in the file i uploaded. The design should include a front and back label.

Target Market(s)

Brell Fine Wines are targeting middle class wine drinkers in 2nd-4th tier Chinese cities.

Colors

Designer to choose colors to be used in the design.

Requirements
Must have
• We’d like something that at first glance is Australian (element, style or color…) but subconsciously connects to the Chinese. Demeanor bearing in mind the demographics targeted across the ranges. We would expect the designs and naming to becoming more formalized as they rise to platinum.
Nice to have
• creative things come out
Should not have
• any dead related word or icon, no number '4' related word or icon, no skull related word or icon, kangaroo (see brand 'Copper vine')

```html
<!DOCTYPE html>
<html lang="en">
<head>
<meta charset="utf-8">
<title>Brell Fine Wine – Solva Vintage 2007 Label</title>
<link rel="stylesheet" href="https://fonts.googleapis.com/css2?family=Marcellus&family=Cinzel:wght@400;600&family=Open+Sans:wght@600;700&display=swap">
<style>
  :root {
    --backdrop: #ececec;
    --label-white: #f7f7f7;
    --wine-red: #c8161d;
    --red-light: #e9585a;
    --red-deep: #b80f16;
    --ink: #333333;
    --rule: #8a8a8a;
  }
  * { margin: 0; padding: 0; box-sizing: border-box; }
  html, body {
    width: 1200px;
    height: 1200px;
    overflow: hidden;
    background: var(--backdrop);
  }
  .canvas {
    position: relative;
    width: 1200px;
    height: 1200px;
  }
  .label-art {
    position: absolute;
    inset: 0;
  }
  .label-text {
    position: absolute;
    left: 0;
    width: 1200px;
    text-align: center;
  }
  .producer {
    top: 556px;
    font-family: 'Open Sans', sans-serif;
    font-weight: 700;
    font-size: 34px;
    color: var(--wine-red);
    letter-spacing: 0.5px;
  }
  .wine-name {
    top: 660px;
    font-family: 'Marcellus', serif;
    font-size: 150px;
    line-height: 150px;
    color: var(--wine-red);
    letter-spacing: 10px;
  }
  .vintage {
    top: 838px;
    font-family: 'Cinzel', serif;
    font-weight: 400;
    font-size: 48px;
    color: var(--ink);
    letter-spacing: 2px;
  }
  .grapes {
    top: 900px;
    font-family: 'Open Sans', sans-serif;
    font-weight: 600;
    font-size: 15px;
    color: var(--ink);
    letter-spacing: 0.5px;
  }
  .edition-text {
    font-family: 'Open Sans', sans-serif;
    font-weight: 700;
    font-size: 25px;
    fill: var(--wine-red);
    letter-spacing: 1px;
  }
</style>
</head>
<body>
<main class="canvas">
  <svg class="label-art" width="1200" height="1200" viewBox="0 0 1200 1200" xmlns="http://www.w3.org/2000/svg">
    <defs>
      <clipPath id="label-outline">
        <path d="M151,162 H400 C410,162 410,120 430,105 Q600,78 770,105 C790,120 790,162 800,162 H1049 Q1059,162 1059,172 V1013 Q1059,1023 1049,1023 H790 C780,1023 780,1060 760,1075 Q600,1125 440,1075 C420,1060 420,1023 410,1023 H151 Q141,1023 141,1013 V172 Q141,162 151,162 Z"/>
      </clipPath>
      <linearGradient id="band-gradient" x1="0" y1="0" x2="1" y2="0">
        <stop offset="0" stop-color="var(--red-light)"/>
        <stop offset="0.5" stop-color="var(--wine-red)"/>
        <stop offset="1" stop-color="var(--red-deep)"/>
      </linearGradient>
      <path id="edition-arc" d="M505,1020 Q600,1075 705,1010"/>
    </defs>

    <g class="label-body" clip-path="url(#label-outline)">
      <rect class="label-paper" x="100" y="60" width="1000" height="1100" fill="var(--label-white)"/>
      <rect class="landscape-band" x="100" y="60" width="1000" height="432" fill="url(#band-gradient)"
            role="img" aria-label="Illustration: white silhouette of a large tree in an open landscape with animals running across the plain"/>
    </g>

    <g class="producer-rules" stroke="var(--wine-red)" stroke-width="2">
      <line x1="455" y1="548" x2="745" y2="548"/>
      <line x1="455" y1="600" x2="745" y2="600"/>
    </g>

    <line class="vintage-rule" x1="411" y1="932" x2="800" y2="932" stroke="var(--rule)" stroke-width="2"/>

    <text class="edition-text">
      <textPath href="#edition-arc" startOffset="50%" text-anchor="middle">SPECIAL EDITION</textPath>
    </text>
  </svg>

  <p class="label-text producer">BRELL FINE WINE</p>
  <h1 class="label-text wine-name">SOLVA</h1>
  <p class="label-text vintage">Vintage 2007</p>
  <p class="label-text grapes">MERLOT &amp; CABERNET SAUVIGNON GRAPES</p>
</main>
</body>
</html>
```